VelliFilez Website

VelliFiles - Orderly Medical Filez
We need a Web design for a new company called - VelliFilez.
VelliFilez is a Personal Injury and Medical Record Legal Service Outsourcing company. We help Personal Injury Attorneys - with fact based Medical Chronologies and Summaries.

We take Medical Records in disarray and put them in order and summarize them in a chronological order and Update them as needed (if more medical records are added)
Take Releases (for medical records) and work with doctor practices and get the records if needed

Target Market(s)

Personal Injury Attorneys

Industry/Entity Type

Attorney

Number of Pages Required

2 page

Font styles to use
Serif
Sans Serif

Colors

Designer to choose colors to be used in the design.

Requirements
Must have
• Professional Design
• Just need the design for the Home page and Internal pages - I will do the Coding for the pages in html and/or wordpress.
• Don't worry about the content - just need a design.

```html
<!DOCTYPE html>
<html lang="en">
<head>
<meta charset="utf-8">
<title>VelliFilez</title>
<link href="https://fonts.googleapis.com/css2?family=Dosis:wght@400;500;600;700&display=swap" rel="stylesheet">
<style>
:root{
  --teal:#1b8d9c;
  --teal-dark:#0d4d58;
  --ink:#2f3b40;
  --text:#555f63;
  --muted:#8a9498;
  --white:#ffffff;
  --page:#f3f5f6;
  --mint-a:#e8f6f3;
  --mint-b:#a9ddd8;
}
*{box-sizing:border-box;margin:0;padding:0}
html,body{width:1200px;height:3209px;overflow:hidden}
body{position:relative;font-family:"Dosis",sans-serif;color:var(--text);background:var(--page)}
.abs{position:absolute}

/* header & hero */
.hero{left:0;top:0;width:1200px;height:571px;background:linear-gradient(160deg,#3d4347 0%,#24282b 45%,#4a4f52 70%,#1b1e20 100%)}
.hero-tint{left:0;top:250px;width:1200px;height:321px;background:linear-gradient(90deg,rgba(190,150,40,.25),rgba(190,150,40,.1) 60%,rgba(0,0,0,0))}
.nav{left:86px;top:43px;width:1024px;height:53px;background:var(--white);display:flex;justify-content:flex-end;align-items:center;padding-right:26px}
.nav a{font-size:14px;color:var(--ink);text-decoration:none;width:120px;text-align:center}
.logo{left:86px;top:30px;width:158px;height:81px;background:var(--white);display:flex;justify-content:center;align-items:center;box-shadow:0 2px 6px rgba(0,0,0,.25)}
.logo-name{font-size:25px;font-weight:700;color:var(--teal-dark);letter-spacing:.5px}
.hero-band{left:86px;top:443px;width:1024px;height:128px;background:var(--teal);display:flex;align-items:center;justify-content:center;text-align:center;padding:0 20px}
.hero-band h1{color:var(--white);font-size:33px;font-weight:600;line-height:43px;letter-spacing:1px;text-transform:uppercase}
.hero-sub{left:86px;top:571px;width:1024px;height:73px;background:var(--white);box-shadow:0 2px 4px rgba(0,0,0,.15);text-align:center;padding:6px 40px;font-size:13px;line-height:29px;color:var(--muted);font-weight:500}

/* intro sections */
.photo{background:linear-gradient(135deg,#f4f4f4,#c9ccce);box-shadow:0 1px 6px rgba(0,0,0,.3)}
.accent-l{width:9px;background:var(--teal)}
.accent-b{height:9px;background:var(--teal)}
.sec-title{font-size:32px;font-weight:500;color:var(--teal);letter-spacing:1px;text-transform:uppercase}
.copy{font-size:13.5px;line-height:21px;color:var(--text)}
.divider{left:86px;top:1067px;width:1024px;height:1px;background:#d7dbdd}

/* services */
.services{left:0;top:1500px;width:1200px;height:1191px;background:linear-gradient(170deg,#f2faf7 0%,var(--mint-a) 20%,var(--mint-b) 100%)}
.center-title{left:0;width:1200px;text-align:center;font-size:35px;font-weight:600;color:var(--teal-dark);letter-spacing:1px}
.card{left:86px;width:1024px;height:173px;background:var(--white);box-shadow:0 2px 5px rgba(0,0,0,.15)}
.card .thumb{position:absolute;top:0;width:175px;height:173px}
.card h3{position:absolute;top:26px;font-size:18px;font-weight:600;color:var(--ink);letter-spacing:.5px}
.card p{position:absolute;top:65px;font-size:13px;line-height:21px;color:var(--text)}
.card a{position:absolute;bottom:18px;font-size:14px;font-weight:600;color:var(--teal);text-decoration:underline}
.card.left .thumb{left:0}
.card.left h3{left:211px}
.card.left p{left:211px;right:16px}
.card.left a{right:16px}
.card.right .thumb{right:0}
.card.right h3{right:211px}
.card.right p{left:16px;right:211px;text-align:right}
.card.right a{left:16px}
.btn{background:var(--teal);color:var(--white);font-size:13px;font-weight:600;display:flex;align-items:center;justify-content:center;letter-spacing:.5px;text-transform:uppercase}

/* contact */
.contact{left:0;top:2691px;width:1200px;height:458px;background:linear-gradient(180deg,#eef1f2,#f7f8f9)}
.field{background:var(--white);box-shadow:0 1px 4px rgba(0,0,0,.2);font-size:11px;color:var(--muted);padding:14px;text-transform:uppercase;letter-spacing:.5px}
.footer{left:0;top:3149px;width:1200px;height:60px;background:var(--teal-dark);color:var(--white);font-size:14px;font-weight:600;display:flex;align-items:center;justify-content:center}
</style>
</head>
<body>

<header>
  <div class="abs hero" role="img" aria-label="Photo of open filing cabinet drawers full of yellow folders"></div>
  <div class="abs hero-tint"></div>
  <nav class="abs nav">
    <a href="#">Menu 01</a><a href="#">Menu 02</a><a href="#">Menu 03</a><a href="#">Menu 04</a><a href="#">Menu 05</a><a href="#">Menu 06</a>
  </nav>
  <div class="abs logo"><span class="logo-name">VelliFilez</span></div>
  <div class="abs hero-band"><h1>Lorem Ipsum is simply dummy text of the printing and type-setting</h1></div>
  <div class="abs hero-sub">Lorem Ipsum is simply dummy text of the printing and typesetting Lorem Ipsum is simply dummy text of the printing and typesetting Lorem Ipsum is Lorem Ipsum is simply dummy text of the printing and typesetting Lorem Ipsum is simply dummy</div>
</header>

<section class="welcome">
  <div class="abs accent-l" style="left:265px;top:883px;height:134px"></div>
  <div class="abs accent-b" style="left:265px;top:1008px;width:135px"></div>
  <div class="abs photo" style="left:272px;top:697px;width:282px;height:313px" role="img" aria-label="Photo of a long row of white ring binders"></div>
  <h2 class="abs sec-title" style="left:582px;top:738px">Welcome</h2>
  <p class="abs copy" style="left:582px;top:806px;width:355px">Lorem Ipsum is simply dummy text of the printing and typesetting industry. Lorem Ipsum has been the industry's standard dummy text ever since the 1500s, when an unknown printer took a galley of type and scrambled it to make. Lorem Ipsum is simply dummy text of the printing and typesetting industry. Lorem Ipsum has been the industry's standard dummy text ever since the 1500s, whe.</p>
</section>

<div class="abs divider"></div>

<section class="about">
  <h2 class="abs sec-title" style="left:261px;top:1166px">About Us</h2>
  <p class="abs copy" style="left:261px;top:1233px;width:350px">Lorem Ipsum is simply dummy text of the printing and typesetting industry. Lorem Ipsum has been the industry's standard dummy text ever since the 1500s, when an unknown printer took a galley of type and scrambled it to make. Lorem Ipsum is simply dummy text of the printing and typesetting industry. Lorem Ipsum has been the industry's standard dummy text ever since the 1500s, whe.</p>
  <div class="abs accent-l" style="left:926px;top:1310px;height:136px"></div>
  <div class="abs accent-b" style="left:801px;top:1437px;width:134px"></div>
  <div class="abs photo" style="left:648px;top:1127px;width:278px;height:308px;background:linear-gradient(135deg,#1c3a6e,#2d6ea8 50%,#0f2448)" role="img" aria-label="Illustration of medical icons in glowing blue hexagons"></div>
</section>

<section class="abs services">
  <h2 class="abs center-title" style="top:42px">OUR SERVICES</h2>
</section>

<article class="abs card left" style="top:1615px">
  <div class="thumb" role="img" aria-label="Photo of red and black lever arch files" style="background:linear-gradient(90deg,#c8262a 0 30%,#2a2a2a 30% 100%)"></div>
  <h3>LOREM IPSUM IS SIMPLY DUMMY</h3>
  <p>Lorem Ipsum is simply dummy text of the printing and typesetting industry. Lorem Ipsum has been the industry's standard dummy text ever since the 1500s, when an unknown printer took a galley of type and scrambled it to make. Lorem Ipsum is simply dummy text of the printing and typesetting industry. Lorem Ipsum has been the industry's standard dummy text.</p>
  <a href="#">Read More...</a>
</article>

<article class="abs card right" style="top:1814px">
  <div class="thumb" role="img" aria-label="Photo of a hand writing on a blue clipboard" style="background:linear-gradient(135deg,#d9a56b,#f1ede6 45%,#2f6fb8)"></div>
  <h3>LOREM IPSUM IS SIMPLY DUMMY</h3>
  <p>Lorem Ipsum is simply dummy text of the printing and typesetting industry. Lorem Ipsum has been the industry's standard dummy text ever since the 1500s, when an unknown printer took a galley of type and scrambled it to make. Lorem Ipsum is simply dummy text of the printing and typesetting industry. Lorem Ipsum has been the industry's standard dummy text.</p>
  <a href="#">Read More...</a>
</article>

<article class="abs card left" style="top:2011px">
  <div class="thumb" role="img" aria-label="Photo of a stethoscope on blue medical paperwork" style="background:linear-gradient(135deg,#c7dcef,#7aa6d0 60%,#e9f0f6)"></div>
  <h3>LOREM IPSUM IS SIMPLY DUMMY</h3>
  <p>Lorem Ipsum is simply dummy text of the printing and typesetting industry. Lorem Ipsum has been the industry's standard dummy text ever since the 1500s, when an unknown printer took a galley of type and scrambled it to make. Lorem Ipsum is simply dummy text of the printing and typesetting industry. Lorem Ipsum has been the industry's standard dummy text.</p>
  <a href="#">Read More...</a>
</article>

<article class="abs card right" style="top:2207px">
  <div class="thumb" role="img" aria-label="Photo of a hand with a pen beside a laptop keyboard" style="background:linear-gradient(135deg,#3a3d40,#9ea3a6 45%,#f3f3f3)"></div>
  <h3>LOREM IPSUM IS SIMPLY DUMMY</h3>
  <p>Lorem Ipsum is simply dummy text of the printing and typesetting industry. Lorem Ipsum has been the industry's standard dummy text ever since the 1500s, when an unknown printer took a galley of type and scrambled it to make. Lorem Ipsum is simply dummy text of the printing and typesetting industry. Lorem Ipsum has been the industry's standard dummy text.</p>
  <a href="#">Read More...</a>
</article>

<article class="abs card left" style="top:2404px">
  <div class="thumb" role="img" aria-label="Photo of a red binder among white binders" style="background:linear-gradient(90deg,#e6e6e6 0 25%,#d42b2b 25% 80%,#efefef 80%)"></div>
  <h3>LOREM IPSUM IS SIMPLY DUMMY</h3>
  <p>Lorem Ipsum is simply dummy text of the printing and typesetting industry. Lorem Ipsum has been the industry's standard dummy text ever since the 1500s, when an unknown printer took a galley of type and scrambled it to make. Lorem Ipsum is simply dummy text of the printing and typesetting industry. Lorem Ipsum has been the industry's standard dummy text.</p>
  <a href="#">Read More ...</a>
</article>

<div class="abs btn" style="left:539px;top:2601px;width:122px;height:36px">Load More</div>

<section class="abs contact">
  <h2 class="abs center-title" style="top:43px">CONTACT US</h2>
  <div class="abs field" style="left:105px;top:113px;width:481px;height:47px">Name</div>
  <div class="abs field" style="left:614px;top:113px;width:477px;height:47px">Email</div>
  <div class="abs field" style="left:105px;top:177px;width:986px;height:172px">Message</div>
  <div class="abs btn" style="left:486px;top:370px;width:228px;height:36px">Send Message</div>
</section>

<footer class="abs footer">Copyright © VelliFilez | All Rights Reserved</footer>

</body>
</html>
```